Brantham Carpets Ltd

I'm looking for a modern looking business card with a logo that's relates to the business, maybe a sheep etc. I will need my name and phone numbers to be included

Industry/Entity Type

Business

Contact Information for Business Card

Neil Brantham, Director
Phone numbers mobile 07931 642058 and office 0161 735 2846
Carpets and flooring supplied and fitted

```html
<!DOCTYPE html>
<html lang="en">
<head>
<meta charset="utf-8">
<title>Brantham Carpets Ltd — Business Card</title>
<link rel="stylesheet" href="https://fonts.googleapis.com/css2?family=Oswald:wght@500&family=Raleway:wght@300;400&display=swap">
<style>
  :root {
    --navy: #1f3150;
    --navy-deep: #192840;
    --card: #f7f7f5;
    --backdrop: #e9e6e1;
    --ink-light: #ffffff;
    --ink-soft: #d9dfe8;
    --fleece: #e4e4e2;
  }
  * { box-sizing: border-box; margin: 0; padding: 0; }
  html, body {
    width: 1200px; height: 800px; overflow: hidden;
    background: var(--backdrop);
  }
  .canvas {
    width: 1200px; height: 800px;
    display: flex; align-items: center; justify-content: center; gap: 40px;
  }
  .card {
    width: 540px; height: 340px;
    background: var(--card);
    box-shadow: 0 6px 18px rgba(0,0,0,.12);
    position: relative;
  }
  .card-front .panel {
    position: absolute; inset: 28px;
    background: radial-gradient(ellipse at 50% 30%, var(--navy) 0%, var(--navy-deep) 100%);
    display: flex; flex-direction: column; align-items: center; justify-content: center;
  }
  .mark-dot {
    width: 86px; height: 86px; border-radius: 50%;
    background: var(--fleece);
    margin-bottom: 22px;
  }
  .wordmark {
    font-family: "Oswald", sans-serif; font-weight: 500;
    text-transform: uppercase; letter-spacing: .42em;
    font-size: 19px; color: var(--ink-light);
    margin-right: -.42em;
  }
  .tagline {
    font-family: "Raleway", sans-serif; font-weight: 300;
    text-transform: uppercase; letter-spacing: .03em;
    font-size: 12.5px; color: var(--ink-soft);
    margin-top: 8px;
  }
  .card-back .brand {
    position: absolute; top: 18px; left: 0; right: 0;
    display: flex; flex-direction: column; align-items: center;
  }
  .card-back .mark-dot { width: 34px; height: 34px; margin-bottom: 8px; background: #cfd2d6; }
  .card-back .wordmark { color: var(--navy); font-size: 15px; }
  .card-back .tagline { color: var(--navy); font-size: 10px; margin-top: 4px; font-weight: 400; }
  .card-back .panel {
    position: absolute; left: 28px; right: 28px; top: 128px; bottom: 28px;
    background: var(--navy);
    display: flex; flex-direction: column; align-items: center; justify-content: center;
    color: var(--ink-light);
  }
  .person {
    font-family: "Oswald", sans-serif; font-weight: 500;
    text-transform: uppercase; font-size: 19px; letter-spacing: .02em;
  }
  .role {
    font-family: "Raleway", sans-serif; font-weight: 400;
    text-transform: uppercase; font-size: 13px; margin-bottom: 12px;
  }
  .contacts {
    font-family: "Raleway", sans-serif; font-weight: 400;
    font-size: 12.5px; line-height: 1.55; list-style: none;
  }
</style>
</head>
<body>
<main class="canvas">
  <section class="card card-front">
    <div class="panel">
      <div class="mark-dot" role="img" aria-label="Brand mark area"></div>
      <h1 class="wordmark">Brantham Carpets Ltd</h1>
      <p class="tagline">Carpets and flooring supplied and fitted</p>
    </div>
  </section>
  <section class="card card-back">
    <div class="brand">
      <div class="mark-dot" role="img" aria-label="Brand mark area"></div>
      <p class="wordmark">Brantham Carpets Ltd</p>
      <p class="tagline">Carpets and flooring supplied and fitted</p>
    </div>
    <div class="panel">
      <h2 class="person">Neil Brantham</h2>
      <p class="role">Director</p>
      <ul class="contacts">
        <li>mobile: 07931 642058</li>
        <li>office: 0161 735 2846</li>
      </ul>
    </div>
  </section>
</main>
</body>
</html>
```